Corporate Branding for Professional Services Company

This project is logo design, business card deisgn and letterhead design.

My client is a company name called Brightmere Staffing Ireland and they are a professional services company that provide the following services:

- Field Sales
- Merchandising
- Promotional Events & Demo's
- Sales Training
- Mystery Shopper
- POS placement & Mangement
- Field Marketing

Their target market is high end corporate companies so the logo, letterhead and business card will need to be very professional corporate looking. The idea that I pitched to them was that they are provision "Vision" to their clients, so how about putting a lighthouse in the logo with the name, possibly the lighthouse emitting a light trail also? Its an idea, play with it!

The colours are black with another complementing colour of your choice, definitely no pinks!

I need this designs done asap please.

Target Market(s)

Corporate Businesses, Professinoal Services company

Industry/Entity Type

Business Consultant

Font styles to use
Serif
Sans Serif

Requirements
Must have
• Professorial corporate Classy look and feel to it. Dark colours.
Should not have
• No Pink

```html
<!DOCTYPE html>
<html lang="en">
<head>
<meta charset="utf-8">
<title>Brightmere Staffing Ireland – Stationery</title>
<link rel="stylesheet" href="https://fonts.googleapis.com/css2?family=Cinzel:wght@400&family=Lato:wght@400&display=swap">
<style>
  :root {
    --ink: #111111;
    --paper: #ffffff;
    --stage: #ffffff;
    --grey: #9a9a9a;
    --soft-grey: #c9c9c9;
    --card-text: #e6e6e6;
  }
  * { margin: 0; padding: 0; box-sizing: border-box; }
  html, body { width: 779px; height: 1200px; overflow: hidden; background: var(--stage); }
  .canvas { position: relative; width: 779px; height: 1200px; }
  .serif { font-family: "Cinzel", "Times New Roman", serif; font-weight: 400; }
  .sans { font-family: "Lato", Arial, sans-serif; font-weight: 400; }

  /* Brand lockup */
  .brand-lockup { position: absolute; left: 0; top: 30px; width: 779px; text-align: center; color: var(--ink); }
  .brand-mark { width: 96px; height: 96px; border: 2px solid var(--ink); border-radius: 50%; margin: 0 auto 24px; }
  .brand-name { font-size: 30px; letter-spacing: 1px; line-height: 1.1; white-space: nowrap; }
  .brand-sub { font-size: 11px; letter-spacing: 7px; margin-top: 4px; }

  /* Business cards */
  .card { position: absolute; top: 229px; width: 178px; height: 104px; background: var(--ink); border: 1px solid #444; color: var(--card-text); overflow: hidden; }
  .card-front { left: 229px; text-align: center; }
  .card-back { left: 416px; }
  .card-brand-dot { width: 14px; height: 14px; border: 1px solid var(--card-text); border-radius: 50%; margin: 10px auto 3px; }
  .card-brand { font-size: 5px; letter-spacing: .4px; white-space: nowrap; }
  .card-name { font-size: 9px; margin-top: 9px; letter-spacing: .6px; white-space: nowrap; }
  .card-role { font-size: 4.5px; letter-spacing: .5px; margin-top: 2px; }
  .card-phone { font-size: 4.5px; margin-top: 5px; }
  .card-contact { font-size: 4.5px; margin-top: 10px; line-height: 1.5; letter-spacing: .3px; }
  .service-list { list-style: none; position: absolute; left: 12px; top: 16px; font-size: 4.6px; line-height: 1.75; text-transform: uppercase; letter-spacing: .3px; }
  .card-back-mark { position: absolute; right: 22px; top: 22px; width: 40px; height: 40px; border: 1px solid #555; border-radius: 50%; }

  /* Letterhead */
  .letterhead { position: absolute; left: 164px; top: 360px; width: 452px; height: 784px; background: var(--paper); box-shadow: 0 0 4px rgba(0,0,0,.35); overflow: hidden; }
  .letterhead svg { position: absolute; inset: 0; }
  .sender { position: absolute; right: 18px; top: 22px; text-align: right; color: var(--card-text); }
  .sender-name { font-size: 15px; letter-spacing: 1px; white-space: nowrap; }
  .sender-role { font-size: 8px; letter-spacing: 1px; margin-top: 2px; }
  .sender-phone { font-size: 6px; margin-top: 14px; }
  .centre-brand { position: absolute; left: 0; top: 280px; width: 452px; text-align: center; color: var(--grey); }
  .centre-mark { width: 80px; height: 80px; border: 2px solid var(--soft-grey); border-radius: 50%; margin: 0 auto 20px; }
  .centre-name { font-size: 24px; letter-spacing: 1px; line-height: 1.1; white-space: nowrap; }
  .centre-sub { font-size: 10px; letter-spacing: 6px; margin-top: 4px; }
  .footer-contact { position: absolute; left: 14px; bottom: 14px; color: var(--card-text); font-size: 6px; line-height: 1.55; letter-spacing: .3px; text-transform: uppercase; }
</style>
</head>
<body>
<main class="canvas">

  <header class="brand-lockup">
    <div class="brand-mark"></div>
    <div class="brand-name serif">Brightmere Staffing</div>
    <div class="brand-sub serif">IRELAND</div>
  </header>

  <section class="card card-front">
    <div class="card-brand-dot"></div>
    <div class="card-brand serif">Brightmere Staffing Ireland</div>
    <div class="card-name serif">AOIFE KEARNEY</div>
    <div class="card-role serif">DIRECTOR</div>
    <div class="card-phone sans">086 555 0142</div>
    <div class="card-contact sans">info@brightmerestaffing.ie<br>www.brightmerestaffing.ie</div>
  </section>

  <section class="card card-back">
    <ul class="service-list sans">
      <li>Field Sales</li>
      <li>Merchandising</li>
      <li>Promotional Events &amp; Demos</li>
      <li>Sales Training</li>
      <li>Mystery Shopper</li>
      <li>POS Placement &amp; Management</li>
      <li>Field Marketing</li>
    </ul>
    <div class="card-back-mark"></div>
  </section>

  <section class="letterhead">
    <svg viewBox="0 0 452 784" width="452" height="784" aria-hidden="true">
      <path d="M150 0 H452 V190 C410 80 300 22 150 0 Z" fill="var(--ink)"/>
      <path d="M132 0 C300 26 418 96 452 214" fill="none" stroke="var(--soft-grey)" stroke-width="1.5"/>
      <path d="M0 560 C36 680 150 756 300 784 H0 Z" fill="var(--ink)"/>
      <path d="M0 536 C42 670 164 756 324 784" fill="none" stroke="var(--soft-grey)" stroke-width="1.5"/>
    </svg>
    <div class="sender">
      <div class="sender-name serif">AOIFE KEARNEY</div>
      <div class="sender-role serif">DIRECTOR</div>
      <div class="sender-phone sans">086 555 0142</div>
    </div>
    <div class="centre-brand">
      <div class="centre-mark"></div>
      <div class="centre-name serif">Brightmere Staffing</div>
      <div class="centre-sub serif">IRELAND</div>
    </div>
    <div class="footer-contact sans">
      info@brightmerestaffing.ie<br>
      www.brightmerestaffing.ie<br>
      4 Harbour Row, Kilbarra, Co. Glenmore
    </div>
  </section>

</main>
</body>
</html>
```